Very dated, simple professional product website needs updating/reskinning of template

Our client currently has a very simple website at www.brightpitch9homes.com that is very, very dated, uses flash, and the template needs to have an updated look for 2014. It needs to look professional, corporate, strong colors, and if using images, actors must have a very well dressed look, etc. Client likes the layout (but not necessarily the colors, etc.) of another similar product site, www.dwellkitpro.com, for example.

The Brightpitch product is an online "presentation document builder" that uses up-to-date content for agents to create 20 - 40 page presentations for potential clients. Real estate agents pay $500+ one-time plus $85/year to use the service, so the website look needs to be consistent with a $500+ product. All of the content will stay essentially the same for now: the goal is to simply re-skin the site to make it look modern, ideally through the use of new CSS files and images, and maybe some script. But we do not want to recode the whole thing, just update the template.

The site layout also needs to work with mobile devices, and so the flash has to be removed, but there is still a need to have possibly a slideshow or something to quickly grab the attention of people who visit the site so they can very quickly understand what the product is.

Also, the plan is to cut down on some of the menu buttons and/or rename them to be more compelling. There are pages on the site that can only be viewed after logging in, and we will want to use the template for those secure pages also.

Reason: My clients have requested that we see if we can get a few more designs to choose between, and to provide them with some time to mull over the current designs.

Reason: My client has requested that we continue to seek designs.

Product

```html
<!DOCTYPE html>
<html lang="en">
<head>
<meta charset="utf-8">
<title>Brightpitch 4 Real Estate</title>
<link href="https://fonts.googleapis.com/css2?family=Arimo:wght@400;700&display=swap" rel="stylesheet">
<style>
:root{
  --ink:#111;
  --black:#000;
  --blue:#123a8f;
  --blue-deep:#0d2f7c;
  --grey:#777;
  --grey-dark:#444;
  --rule:#dcdcdc;
  --paper:#fff;
  --footer-text:#cfcfcf;
}
*{margin:0;padding:0;box-sizing:border-box}
html,body{width:1016px;height:1200px;overflow:hidden;background:var(--paper)}
body{position:relative;font-family:'Arimo',Arial,sans-serif;color:var(--ink)}
a{color:inherit;text-decoration:none}
.abs{position:absolute}

.topbar{left:0;top:0;width:1016px;height:20px;background:var(--black);color:#ddd;font-size:10px;line-height:20px}
.topbar .links{position:absolute;right:136px;top:0}
.topbar .links span.sep{margin:0 6px}
.topbar .active{color:#fff;text-decoration:underline}

.header{left:0;top:20px;width:1016px;height:83px;background:linear-gradient(90deg,#fff 0%,#f4f5f7 60%,#fff 100%)}
.header-rule{left:0;top:103px;width:1016px;height:3px;background:var(--blue)}
.brand{left:137px;top:44px;font-size:26px;font-weight:400;color:var(--black);line-height:30px;white-space:nowrap}
.help{right:136px;top:40px;font-size:11px;font-weight:700;color:#222;display:flex;align-items:center;gap:5px}
.help .phone{font-weight:400;font-size:13px;color:var(--blue)}
.nav{left:443px;top:74px;font-size:11px;color:#111;display:flex}
.nav a{margin-right:22px}
.nav a.current{color:var(--blue);position:relative}
.nav a.current::after{content:"";position:absolute;left:18px;top:23px;border:5px solid transparent;border-bottom-color:var(--blue);border-top:0}

.hero{left:0;top:106px;width:1016px;height:374px;background:
  radial-gradient(ellipse 330px 200px at 640px 170px,#d8c4aa 0%,#a9785a 45%,transparent 75%),
  linear-gradient(180deg,#8fa9d2 0%,#c8d3e4 40%,#e6ddcf 75%,#d9cdbb 100%)}
.arrow{width:40px;height:40px;border-radius:50%;border:2px solid #fff;background:rgba(255,255,255,.85);display:flex;align-items:center;justify-content:center}
.caption{background:var(--black);color:#fff;font-size:17px;line-height:25px;padding:0 7px}

.h2{font-size:19px;font-weight:400;color:var(--black);line-height:22px}
.h2 em{font-style:normal;color:var(--blue)}
.sub{font-size:11px;color:#333;letter-spacing:.2px}
.rule{height:1px;background:var(--rule)}
.body-text{font-size:10px;line-height:13.4px;color:var(--grey);text-align:justify;letter-spacing:.4px}
.btn{background:var(--blue-deep);color:#fff;font-size:10px;line-height:20px;height:20px;padding:0 7px;display:inline-block;letter-spacing:.3px}
.divider{left:583px;top:508px;width:1px;height:572px;background:var(--rule)}

.video{left:136px;top:816px;width:408px;height:264px;background:#e4e4e4;padding:5px}
.video .screen{position:relative;width:398px;height:254px;background:
  radial-gradient(ellipse 120px 80px at 200px 100px,#c7472a 0%,transparent 80%),
  linear-gradient(180deg,#c98644 0%,#b45b2a 45%,#7a2418 100%)}
.video .controls{position:absolute;left:0;bottom:0;width:100%;height:12px;background:rgba(220,220,220,.85)}
.play{position:absolute;left:180px;top:110px;width:38px;height:38px;border-radius:50%;background:#fff;border:2px solid #333;display:flex;align-items:center;justify-content:center}

.thumb{width:85px;height:94px;border:2px solid #ddd;background:linear-gradient(135deg,#222,#000 60%,#333)}
.prod-title{font-size:10px;font-weight:700;color:#444;line-height:11.5px;letter-spacing:.4px}
.prod-title span{font-weight:400}
.price{font-size:10px;font-weight:700;color:var(--blue);line-height:11.5px;letter-spacing:.4px}
.price-note{font-size:10px;color:#555;line-height:11.5px;letter-spacing:.4px}

.quote{left:623px;top:922px;width:244px;font-size:9.6px;line-height:13.4px;color:#444;letter-spacing:.15px}
.qmark{font-size:34px;color:#bbb;line-height:20px;font-family:Georgia,serif}
.author{left:795px;top:1024px;font-size:10.5px;font-style:italic;font-weight:700;color:#444}

.footer{left:0;top:1121px;width:1016px;height:79px;background:var(--black)}
.footer-links{left:136px;top:1146px;font-size:10px;line-height:16.5px;color:var(--footer-text)}
.footer-links .sep{margin:0 8px}
.footer-links .current{color:#fff;text-decoration:underline}
.footer-brand{left:690px;top:1144px;font-size:22px;line-height:26px;color:#fff;white-space:nowrap}
.copy{left:842px;top:1152px;font-size:12px;color:#ddd}
</style>
</head>
<body>

<div class="abs topbar">
  <div class="links"><a class="active" href="#">Order Now</a><span class="sep">-</span><a href="#">Members Access</a><span class="sep">-</span><a href="#">Newsletter</a><span class="sep">-</span><a href="#">Contact Us</a></div>
</div>

<header class="abs header"></header>
<div class="abs brand">Brightpitch</div>
<div class="abs help">
  <svg width="11" height="11" viewBox="0 0 24 24"><path fill="#111" d="M6.6 10.8a15.1 15.1 0 0 0 6.6 6.6l2.2-2.2c.3-.3.7-.4 1-.2 1.1.4 2.3.6 3.6.6.6 0 1 .4 1 1V20c0 .6-.4 1-1 1A17 17 0 0 1 3 4c0-.6.4-1 1-1h3.5c.6 0 1 .4 1 1 0 1.3.2 2.5.6 3.6.1.3 0 .7-.2 1z"/></svg>
  Help Center -&nbsp;<span class="phone">604-555-0142</span>
</div>
<nav class="abs nav">
  <a class="current" href="#">About Us</a>
  <a href="#">What is Brightpitch</a>
  <a href="#">Brightpitch Demo</a>
  <a href="#">Peer Reviews</a>
  <a href="#" style="margin-right:0">F.A.Q</a>
</nav>
<div class="abs header-rule"></div>

<section class="abs hero" role="img" aria-label="Photo of a hand holding a small model house in front of a blurred home"></section>
<div class="abs arrow" style="left:48px;top:274px"><svg width="10" height="16"><path d="M9 0 L0 8 L9 16Z" fill="#444"/></svg></div>
<div class="abs arrow" style="left:933px;top:274px"><svg width="10" height="16"><path d="M1 0 L10 8 L1 16Z" fill="#222"/></svg></div>
<div class="abs caption" style="left:136px;top:267px">Where Great</div>
<div class="abs caption" style="left:136px;top:297px;line-height:26px">Presentations Begin ...</div>

<h2 class="abs h2" style="left:136px;top:507px">Welcome to <em>Brightpitch 4 Real Estate</em></h2>
<p class="abs sub" style="left:138px;top:532px">Your business as a AGENT® is selling real estate.</p>
<div class="abs rule" style="left:136px;top:552px;width:408px"></div>
<p class="abs body-text" style="left:136px;top:566px;width:408px">Our job is in helping you convert more prospects into serious clients so you can do what you do - sell more real estate. We offer you compelling materials to enable you to create your own personal Listing Presentations; Buyer Presentations; Pre-Listing Packages; Unique Open House Hand-Outs; Handling Objection materials; a "keeping Sellers informed" system; Marketing Newsletter plus Presentation Know-How. Quite literally, we provide everything you need to impress your prospects and out-shine your competition. Brightpitch was created by veteran B.C. AGENTS® for B.C. AGENTS® who truly desire success.</p>
<a class="abs btn" style="left:137px;top:688px" href="#">Know More About Us</a>

<h2 class="abs h2" style="left:136px;top:767px">Getting <em>The Business</em></h2>
<div class="abs rule" style="left:136px;top:797px;width:408px"></div>
<div class="abs video">
  <div class="screen" role="img" aria-label="Video still of a theatre auditorium with red seats and stage curtain">
    <div class="play"><svg width="12" height="18"><path d="M1 0 L12 9 L1 18Z" fill="#333"/></svg></div>
    <div class="controls">
      <svg width="398" height="12"><g fill="#555"><rect x="68" y="3" width="2" height="7"/><path d="M70 6.5 78 3v7z"/><path d="M88 6.5 95 3v7zM95 6.5 102 3v7z"/><rect x="116" y="3" width="7" height="7"/><path d="M136 3l8 3.5-8 3.5z"/><path d="M157 3l7 3.5-7 3.5zM164 3l7 3.5-7 3.5z"/><path d="M184 3l8 3.5-8 3.5z"/><rect x="192" y="3" width="2" height="7"/><rect x="310" y="4" width="16" height="4" fill="#222"/></g></svg>
    </div>
  </div>
</div>

<div class="abs divider"></div>

<h2 class="abs h2" style="left:623px;top:507px">Products <em>&amp; Pricing</em></h2>
<p class="abs sub" style="left:625px;top:532px">Testimonials</p>
<div class="abs rule" style="left:623px;top:552px;width:257px"></div>

<div class="abs thumb" style="left:623px;top:570px" role="img" aria-label="Product box for the Brightpitch presentation materials"></div>
<div class="abs" style="left:728px;top:569px;width:170px">
  <p class="prod-title">BRIGHTPITCH Presentation<br>Materials <span>(1st full year)</span></p>
  <p class="price" style="margin-top:12px">$585.00 + HST = $655.20</p>
  <p class="price-note">(This is less than $2.00 a day!)</p>
</div>
<a class="abs btn" style="left:728px;top:644px" href="#">View Details</a>
<div class="abs rule" style="left:623px;top:684px;width:257px"></div>

<div class="abs thumb" style="left:623px;top:703px;background:linear-gradient(135deg,#111 0 30%,#f2f2f2 30% 100%)" role="img" aria-label="Stack of newsletter issues"></div>
<div class="abs" style="left:728px;top:701px;width:170px">
  <p class="prod-title">HOMEFRONT NOTES Newsletter<br><span>(6 issues published Bi-monthly)</span></p>
  <p class="price" style="margin-top:12px">$169.00 + HST = $189.28</p>
  <p class="price-note">(For non-members only)</p>
</div>
<a class="abs btn" style="left:728px;top:777px" href="#">View Details</a>
<div class="abs rule" style="left:623px;top:817px;width:257px"></div>

<h2 class="abs h2" style="left:623px;top:862px">Clien`t <em>Feeds</em></h2>
<p class="abs sub" style="left:625px;top:887px">Testimonials</p>
<div class="abs rule" style="left:623px;top:907px;width:257px"></div>
<div class="abs qmark" style="left:622px;top:924px">“</div>
<p class="abs quote" style="text-indent:31px">Success in real estate sales is simple. It's in knowing what to say and how to say it – in a manner that people will heed. Everything else Realtors do is secondary, yet... it's the secondary stuff most Realtors focus on, thus, their lack of the success they desire.</p>
<div class="abs qmark" style="left:862px;top:1000px">”</div>
<p class="abs author">-- Dana Whitlow</p>
<a class="abs btn" style="left:623px;top:1050px" href="#">Read More</a>

<footer class="abs footer"></footer>
<div class="abs footer-links">
  <div><a class="current" href="#">Home</a><span class="sep">-</span>What is Brightpitch<span class="sep">-</span>Brightpitch Demo<span class="sep">-</span>Testimonials<span class="sep">-</span>Free Presentation Tips</div>
  <div>F.A.Q.Contact Us<span class="sep">-</span>Order Brightpitch<span class="sep">-</span>Newsletter<span class="sep">-</span>Privacy Policy<span class="sep">-</span>Terms of Use</div>
</div>
<div class="abs footer-brand">Brightpitch</div>
<div class="abs copy">© 2014</div>

</body>
</html>
```